Trade Show Display Graphic Design Project

We are looking for a design of a trade show display and podium that is color coordinated with our logo and advertisements (attached).
We are a security consulting firm that provides 4 core services:
-Security Assessment and Planning
-Security Design and Engineering
-Managed Security Services
-Security Training
Our look should reflect a highly professional elite level of expertise.
BACKDROP
We are looking for a backdrop trade show display that is a spin off of the print advertisement we are doing in the trade show magazine (attached advertisement KOVA 2016 Ad.pdf). I am looking to emphasize our core services, possibly with an icon to represent each service and keep the "Identifying - Mitigating - Managing - The Threat" as part of the overall display as see in the print advertisement.
The side curved endcaps can be used to show the logo and name vertically but i will ask you to be creative in how you do the design.
The design should be sleek and simple.
PODIUM
The podium I see as our logo. possibly rearranged with the logo art on top and the text on bottom.
Attached are the technical design requirements for the backdrop and podium. Only follow the technical requirements of the documents. All artwork should be sent to me through the craftpanel website.
LINK TO IMAGE IN SUPPLIED PDF
https://www.filecove.net/s/7k2m9p4q81wzeb3/Stockly_58174620_XXL.jpg?dl=0
Target Market(s)
security directors and senior directors
Industry/Entity Type
Security
Other font styles liked:
- Match logo font
Requirements
Must have
- logo, core services

```html
<!DOCTYPE html>
<html lang="en">
<head>
<meta charset="utf-8">
<title>Bastion Consulting — Trade Show Backdrop</title>
<link href="https://fonts.googleapis.com/css2?family=Arimo:wght@700&family=Open+Sans:ital,wght@0,300;0,400;0,600;1,300;1,400&display=swap" rel="stylesheet">
<style>
  :root {
    --bg-deep: #0c0a0a;
    --bg-mid: #2a2626;
    --bg-light: #4a4545;
    --ink: #ffffff;
    --ink-soft: #d9d9d9;
    --accent: #3d9be0;
    --seam: rgba(0,0,0,0.45);
  }
  html, body {
    margin: 0;
    padding: 0;
    width: 1200px;
    height: 684px;
    overflow: hidden;
    background: var(--bg-deep);
  }
  .backdrop {
    position: relative;
    width: 1200px;
    height: 684px;
    overflow: hidden;
    background:
      radial-gradient(ellipse 70% 35% at 48% 52%, rgba(110,104,104,0.55), transparent 70%),
      linear-gradient(180deg, var(--bg-deep) 0%, var(--bg-mid) 42%, var(--bg-light) 55%, var(--bg-mid) 68%, var(--bg-deep) 100%);
    font-family: "Open Sans", sans-serif;
    color: var(--ink);
  }
  .sweep {
    position: absolute;
    inset: 0;
  }
  .seam {
    position: absolute;
    top: 0;
    width: 2px;
    height: 684px;
    background: var(--seam);
  }
  .seam--left { left: 168px; }
  .seam--right { left: 1032px; }

  .hero-photo {
    position: absolute;
    left: 180px;
    top: 0;
    width: 370px;
    height: 590px;
    background: radial-gradient(ellipse 45% 55% at 45% 60%, rgba(20,18,18,0.9), rgba(40,36,36,0.35) 70%, transparent 100%);
  }

  .brand {
    position: absolute;
    display: flex;
    align-items: center;
    gap: 14px;
    white-space: nowrap;
  }
  .brand__mark {
    width: 44px;
    height: 44px;
    border-radius: 50%;
    background: var(--accent);
    flex: none;
  }
  .brand__text {
    display: flex;
    flex-direction: column;
    font-weight: 600;
    color: var(--ink);
    line-height: 1;
  }
  .brand__name {
    font-size: 68px;
    letter-spacing: -1px;
  }
  .brand__tag {
    font-size: 15px;
    letter-spacing: 11px;
    margin-top: 6px;
    text-transform: uppercase;
  }
  .brand--left {
    left: 105px;
    top: 320px;
    transform: translate(-50%, -50%) rotate(-90deg);
  }
  .brand--right {
    left: 1100px;
    top: 325px;
    transform: translate(-50%, -50%) rotate(90deg);
  }

  .tagline {
    position: absolute;
    left: 516px;
    top: 184px;
    display: flex;
    align-items: center;
  }
  .tagline__verbs {
    font-family: "Arimo", sans-serif;
    font-weight: 700;
    font-size: 35px;
    line-height: 36px;
    letter-spacing: -0.3px;
    text-transform: uppercase;
  }
  .tagline__brace {
    width: 30px;
    height: 112px;
    margin: 0 14px 0 8px;
  }
  .tagline__object {
    font-weight: 400;
    font-size: 29px;
    letter-spacing: 0.5px;
    text-transform: uppercase;
  }

  .services {
    position: absolute;
    left: 554px;
    top: 340px;
  }
  .services__title {
    margin: 0 0 8px;
    font-size: 26px;
    font-weight: 600;
    color: var(--accent);
  }
  .services__list {
    list-style: none;
    margin: 0;
    padding: 0 0 0 52px;
  }
  .services__item {
    display: flex;
    align-items: center;
    gap: 12px;
    height: 40px;
    font-size: 26px;
    font-style: italic;
    font-weight: 300;
    color: var(--ink-soft);
  }
  .services__icon {
    width: 24px;
    height: 26px;
    flex: none;
  }
</style>
</head>
<body>
<main class="backdrop">
  <svg class="sweep" width="1200" height="684" viewBox="0 0 1200 684" aria-hidden="true">
    <path d="M560 390 C760 280 980 170 1200 120 L1200 0 L1080 0 C900 120 720 260 560 390 Z" fill="rgba(255,255,255,0.04)"/>
  </svg>
  <div class="seam seam--left"></div>
  <div class="seam seam--right"></div>

  <div class="hero-photo" role="img" aria-label="Photograph of a hand reaching down toward a coiled, striking black snake"></div>

  <div class="brand brand--left">
    <span class="brand__mark"></span>
    <span class="brand__text"><span class="brand__name">bastion</span><span class="brand__tag">Consulting</span></span>
  </div>

  <div class="brand brand--right">
    <span class="brand__mark"></span>
    <span class="brand__text"><span class="brand__name">bastion</span><span class="brand__tag">Consulting</span></span>
  </div>

  <div class="tagline">
    <div class="tagline__verbs">Identifying<br>Mitigating<br>Managing</div>
    <svg class="tagline__brace" viewBox="0 0 30 112" aria-hidden="true">
      <path d="M4 3 C16 3 14 14 14 30 C14 46 16 54 26 56 C16 58 14 66 14 82 C14 98 16 109 4 109" fill="none" stroke="var(--accent)" stroke-width="5" stroke-linecap="round"/>
    </svg>
    <div class="tagline__object">The Threat</div>
  </div>

  <section class="services">
    <h2 class="services__title">Our Services:</h2>
    <ul class="services__list">
      <li class="services__item">
        <svg class="services__icon" viewBox="0 0 24 26" aria-hidden="true"><path d="M12 1 L22 5 V12 C22 18 17 23 12 25 C7 23 2 18 2 12 V5 Z" fill="var(--accent)"/><circle cx="12" cy="12" r="3.5" fill="none" stroke="#fff" stroke-width="2"/></svg>
        Security Consulting
      </li>
      <li class="services__item">
        <svg class="services__icon" viewBox="0 0 24 26" aria-hidden="true"><path d="M12 1 L22 5 V12 C22 18 17 23 12 25 C7 23 2 18 2 12 V5 Z" fill="var(--accent)"/><path d="M12 7 V17 M9 10 H15" stroke="#fff" stroke-width="2"/></svg>
        Security Engineering
      </li>
      <li class="services__item">
        <svg class="services__icon" viewBox="0 0 24 26" aria-hidden="true"><path d="M12 1 L22 5 V12 C22 18 17 23 12 25 C7 23 2 18 2 12 V5 Z" fill="var(--accent)"/><circle cx="12" cy="10" r="3" fill="#fff"/><path d="M6.5 18 C7.5 14.5 16.5 14.5 17.5 18 Z" fill="#fff"/></svg>
        Managed Security
      </li>
      <li class="services__item">
        <svg class="services__icon" viewBox="0 0 24 26" aria-hidden="true"><path d="M12 1 L22 5 V12 C22 18 17 23 12 25 C7 23 2 18 2 12 V5 Z" fill="var(--accent)"/><path d="M12 6.5 L13.6 10.2 L17.5 10.5 L14.5 13 L15.5 17 L12 14.8 L8.5 17 L9.5 13 L6.5 10.5 L10.4 10.2 Z" fill="#fff"/></svg>
        Security Training
      </li>
    </ul>
  </section>
</main>
</body>
</html>
```